Wine label for boutique family-owned winery

We need a front wine label designed for Velmora, our small, family-owned, Oregon based winery . Velmora makes warm climate red blends with grapes sourced from SE Washington state, USA. We are a startup business with wines for 2013 and 2014.

The name Velmora comes from the Georgian language, and is short for Tobias, my father's name. The Georgians have an 5000-8000 year history of winemaking, out of which they give heartfelt toasts that celebrate kinship, family, and loved ones of the past and future.

The design can be of various aspect ratios, but should fit flatly on a bordeaux style wine bottle.
We would like this wine label to work for red wines, and be convertible to work with white wines with some simple background color changes. The preferred file format is Adobe Illustrator. This label will be digitally printed.

A couple wine labels that I like:
- 9 Lanterns
- brelvastudio.com/labels "amber"

I am including a file to show what the existing Velmora label looks like.
Updates

Project Deadline Extended
Reason: To give more time for designer revisions. We want the right design!

Target Market(s)

Direct sales through group tastings.
Professionals aged 30-65 with disposable income.
$35/bottle wine.

Industry/Entity Type

Boutique

Font styles to use
Serif
Decorative
Script

Requirements
Must have
• Rich and/or earthy tones (see link to "Amber" above)
• The text on the front label will include:
• The brand name- Velmora
• Vintage: 2013
• Wine name- Corvalé Blend
• AVA: Washington State
• (The specific information will vary, but we need room for those categories of text.)
Nice to have
• We'd like to convey the qualities of sincerity, trustworthiness, and being grounded. If it's possible to convey our philosophy of sharing wine with friends and family that would be great.
• We have an existing logo "Velmora" that has been attached as an SVG file.
• It is not required to include this logo, but if it works in your design, all the better.
Should not have
• Feature photographs or likenesses of photographs

```html
<!DOCTYPE html>
<html lang="en">
<head>
<meta charset="utf-8">
<title>Velmora — Corvalé Blend 2013 Front Label</title>
<link rel="stylesheet" href="https://fonts.googleapis.com/css2?family=EB+Garamond:wght@400;500&family=Pinyon+Script&display=swap">
<style>
  :root {
    --backdrop: #2a2a2a;
    --label-gold: #d6b655;
    --label-gold-deep: #b89a48;
    --wine-maroon: #7a2826;
    --band-text: #dcbf6a;
  }

  * { margin: 0; padding: 0; box-sizing: border-box; }

  html, body {
    width: 1200px;
    height: 2416px;
    overflow: hidden;
    background: var(--backdrop);
  }

  .canvas {
    position: relative;
    width: 1200px;
    height: 2416px;
  }

  .front-label {
    position: absolute;
    left: 100px;
    top: 592px;
    width: 1000px;
    height: 1232px;
    background: var(--label-gold);
  }

  .brand-name {
    position: absolute;
    right: 50px;
    top: 120px;
    font-family: "EB Garamond", Georgia, serif;
    font-weight: 400;
    font-size: 160px;
    line-height: 1;
    letter-spacing: 2px;
    color: var(--wine-maroon);
  }

  .illustration {
    position: absolute;
    left: 100px;
    top: 300px;
    width: 580px;
    height: 700px;
    border-radius: 6px;
    background: linear-gradient(160deg, rgba(122, 40, 38, 0.28), rgba(122, 40, 38, 0.12));
  }

  .varietal-band {
    position: absolute;
    left: 0;
    bottom: 0;
    width: 100%;
    height: 100px;
    background: var(--wine-maroon);
    display: flex;
    align-items: center;
    padding-left: 40px;
    color: var(--band-text);
  }

  .wine-name {
    font-family: "EB Garamond", Georgia, serif;
    font-size: 66px;
    line-height: 1;
    padding-bottom: 6px;
  }

  .band-divider {
    width: 3px;
    height: 70px;
    margin: 0 20px;
    background: var(--band-text);
  }

  .vintage-block {
    display: flex;
    flex-direction: column;
    align-items: flex-start;
    line-height: 1;
  }

  .vintage {
    font-family: "EB Garamond", Georgia, serif;
    font-size: 56px;
    letter-spacing: 14px;
  }

  .ava {
    font-family: "Pinyon Script", cursive;
    font-size: 26px;
    margin-top: 2px;
  }
</style>
</head>
<body>
  <main class="canvas">
    <section class="front-label">
      <div class="brand-name">Velmora</div>

      <div class="illustration" role="img"
           aria-label="Line illustration of a straw-wrapped wine flask with a cord curling up toward the brand name, beside a decorated stemmed wine glass"></div>

      <div class="varietal-band">
        <span class="wine-name">Corvalé Blend</span>
        <span class="band-divider"></span>
        <div class="vintage-block">
          <span class="vintage">2013</span>
          <span class="ava">Washington State</span>
        </div>
      </div>
    </section>
  </main>
</body>
</html>
```